Tindlemoss - Business Card Design

Hello everyone!

I need a business card design to the following specs:

Size: 2"x2" with .25" bleed

Front:

Logo Attached

Back:

Thank You For Your Purchase!

CLOSET: @tindlemoss

Hottest New Trends
Rare Collectibles + Trinkets
Fashion Accessories and Jewelry
New + Vintage Items
Unique & One of a Kind Pieces

Please submit AI, JPG, and PDF files.

Thank you and good luck!

```html
<!DOCTYPE html>
<html lang="en">
<head>
<meta charset="utf-8">
<title>Tindlemoss – Business Card Front and Back</title>
<link rel="stylesheet" href="https://fonts.googleapis.com/css2?family=Dancing+Script:wght@500&family=Crimson+Pro:wght@500&display=swap">
<style>
  :root {
    --stage: #eef0f1;
    --card-blue: #1f35e6;
    --card-white: #ffffff;
    --brand-red: #e5332a;
    --ink: #1a1a1a;
    --mark-dark: #111111;
  }
  * { box-sizing: border-box; margin: 0; padding: 0; }
  html, body {
    width: 1200px;
    height: 571px;
    overflow: hidden;
    background: var(--stage);
  }
  .canvas {
    position: relative;
    width: 1200px;
    height: 571px;
  }
  .card {
    position: absolute;
    top: 56px;
    width: 458px;
    height: 455px;
    background: var(--card-blue);
  }
  .card--front { left: 56px; }
  .card--back { left: 683px; }

  .panel {
    position: absolute;
    left: 24px;
    right: 24px;
    background: var(--card-white);
  }
  .card--front .panel--top { top: 24px; height: 44px; }
  .card--front .panel--main { top: 91px; height: 277px; }
  .card--front .panel--bottom { top: 392px; height: 43px; }
  .card--back .panel--main { top: 24px; bottom: 24px; }

  .brand-name {
    position: absolute;
    left: 0;
    right: 0;
    text-align: center;
    font-family: "Dancing Script", cursive;
    font-weight: 500;
    color: var(--brand-red);
    line-height: 1;
  }
  .card--front .brand-name { top: 28px; font-size: 50px; }
  .card--back .brand-name { top: 8px; font-size: 54px; }

  .mascot-area {
    position: absolute;
    left: 50%;
    transform: translateX(-50%);
    display: block;
  }
  .card--front .mascot-area { top: 118px; width: 118px; height: 122px; }
  .card--back .mascot-area { top: 93px; width: 112px; height: 116px; }

  .closet-handle {
    position: absolute;
    top: 252px;
    left: 0;
    right: 0;
    text-align: center;
    font-family: "Crimson Pro", serif;
    font-weight: 500;
    font-size: 19px;
    color: var(--ink);
    letter-spacing: 0.2px;
  }
  .offer-list {
    position: absolute;
    top: 280px;
    left: 0;
    right: 0;
    list-style: none;
    text-align: center;
    font-family: "Crimson Pro", serif;
    font-weight: 500;
    font-size: 19px;
    line-height: 25px;
    color: var(--ink);
  }
</style>
</head>
<body>
<main class="canvas">

  <section class="card card--front" aria-label="Card front">
    <div class="panel panel--top"></div>
    <div class="panel panel--main">
      <p class="brand-name">Tindlemoss</p>
      <svg class="mascot-area" viewBox="0 0 118 122" role="img" aria-label="Brand mascot logo artwork">
        <rect width="118" height="122" rx="6" fill="var(--mark-dark)"/>
      </svg>
    </div>
    <div class="panel panel--bottom"></div>
  </section>

  <section class="card card--back" aria-label="Card back">
    <div class="panel panel--main">
      <p class="brand-name">Tindlemoss</p>
      <svg class="mascot-area" viewBox="0 0 112 116" role="img" aria-label="Brand mascot logo artwork">
        <rect width="112" height="116" rx="6" fill="var(--mark-dark)"/>
      </svg>
      <p class="closet-handle">CLOSET: @tindlemoss</p>
      <ul class="offer-list">
        <li>Hottest New Trends</li>
        <li>Rare Collectibles + Trinkets</li>
        <li>Fashion Accessories and Jewelry</li>
        <li>New + Vintage Items</li>
        <li>Unique &amp; One of a Kind Pieces</li>
      </ul>
    </div>
  </section>

</main>
</body>
</html>
```